Tanwick Services Website Design

We have most content but require a professional design. We have a logo already and will need it utilized along with several of the photos from the attached documentation.
First page should have our mission and Vision and the synapsis provided in the word document. Visitors will be prompted to select from one of our 3 divisions from this page.
Each division will have the same list of tabs : About, Services, Safety, Careers and Contact.
Photos on each divisions page should be representative of the divisions offerings. The word doc attached contains the requested content and we are open to edits that would complement and fill the website.
I like the Morvalix site www.morvalix-demo.net - they are our competition so cant be modeled directly after this.
Please include prompts to request quote at each service page. align the format of the geotechnical page to the other 2 divisions.
I used chat gpt for some of the content so will need it optimized for SCO.

```html
<!DOCTYPE html>
<html lang="en">
<head>
<meta charset="UTF-8">
<title>Tanwick Services – Home</title>
<link href="https://fonts.googleapis.com/css2?family=Epilogue:wght@400;500;600;700&display=swap" rel="stylesheet">
<style>
  :root {
    --red: #ed1e24;
    --ink: #1e1e1e;
    --charcoal: #4d4d4d;
    --grey: #9d9e9d;
    --paper: #f0f1f2;
    --backdrop: #d8d8d8;
  }
  * { margin: 0; padding: 0; box-sizing: border-box; }
  html, body {
    width: 894px; height: 1200px; overflow: hidden;
    background: var(--backdrop);
    font-family: "Epilogue", Arial, sans-serif;
  }
  .site {
    position: absolute; left: 20px; top: 333px;
    width: 854px; height: 534px;
    display: flex;
  }
  .intro {
    position: relative; width: 427px; height: 100%;
    background: var(--ink); color: #fff;
  }
  .brand {
    position: absolute; left: 33px; top: 32px;
    font-weight: 700; font-size: 17px; letter-spacing: 1.5px;
    color: var(--red); text-transform: uppercase;
  }
  .headline {
    position: absolute; left: 33px; top: 176px; width: 380px;
    font-weight: 400; font-size: 24.5px; line-height: 30px;
    letter-spacing: -0.1px;
  }
  .headline .accent { color: var(--red); }
  .statements {
    position: absolute; left: 33px; top: 345px;
    display: flex; gap: 21px;
  }
  .statement {
    width: 169px; display: flex; justify-content: space-between; align-items: baseline;
    font-size: 8px; font-weight: 500;
    padding-bottom: 4px; border-bottom: 1px solid var(--red);
  }
  .statement .toggle { font-size: 9px; line-height: 1; }
  .division-label {
    position: absolute; left: 0; right: 0; top: 484px;
    text-align: center; font-size: 7px; color: #ddd;
  }
  .divisions {
    position: absolute; left: 0; bottom: 0; width: 100%; height: 35px;
    display: flex;
  }
  .division {
    display: flex; align-items: center; justify-content: center;
    font-size: 7.5px; font-weight: 500; color: #fff;
  }
  .division.aerial { width: 125px; }
  .division.geotech { width: 147px; background: var(--paper); color: var(--red); }
  .division.renewable { width: 155px; }
  .gallery { width: 427px; height: 100%; display: flex; flex-direction: column; }
  .shot { flex: 1; }
  .shot.town { background: linear-gradient(135deg, #6d6d6d, #858585 50%, #5f5f5f); }
  .shot.crane { background: linear-gradient(120deg, #6a6a6a, #5a5a5a 55%, #444 100%); }
  .shot.site-work { background: linear-gradient(120deg, #747474, #6a6a6a 50%, #858585); }
  .shot.turbine { background: linear-gradient(160deg, #4d4d4d, #575757 60%, #7a7a7a); }
</style>
</head>
<body>
  <main class="site">
    <section class="intro">
      <div class="brand">Tanwick</div>
      <h1 class="headline">Delivering safe, <span class="accent">reliable</span> Aerial Access &amp; Maintenance services to Oil &amp; Gas, Construction, Utility &amp; Renewable Energy Industries</h1>
      <div class="statements">
        <div class="statement"><span>Our Vision</span><span class="toggle">+</span></div>
        <div class="statement"><span>Our Mission</span><span class="toggle">+</span></div>
      </div>
      <p class="division-label">Select Division:</p>
      <nav class="divisions">
        <div class="division aerial">Aerial Access</div>
        <div class="division geotech">Geotechnical Drilling</div>
        <div class="division renewable">Renewable Energy Services</div>
      </nav>
    </section>
    <section class="gallery">
      <div class="shot town" role="img" aria-label="Aerial view of a small town with a company sign on a boom lift"></div>
      <div class="shot crane" role="img" aria-label="Overhead view of a white boom truck casting a long shadow on grass"></div>
      <div class="shot site-work" role="img" aria-label="Aerial view of a work site with trucks, drilling rig and crew"></div>
      <div class="shot turbine" role="img" aria-label="Boom lift reaching up beside a wind turbine"></div>
    </section>
  </main>
</body>
</html>
```